Letterhead Design Project

We are looking for a simple letterhead design that reflects our core purpose. We help our clients gain clarity and focus but we are there to help them execute. The letterhead design would mainly be utilised for engagement letters and contracts.

Target Market(s)

The customers of our business are large corporate organisations.

Requirements
Must have
• The letterhead must have the company logo
The font used must tie in to the font used in the company logo

Must have the following business details
Address: Level 10, 27 Harlow Lane, Melbourne, Australia, 3000
Phone: +61 3 527 948 183
Fax: +61 3 9042 5317
Website: www.bovrin-u.com.au
Twiiter: @bovrin_u

```html
<!DOCTYPE html>
<html lang="en">
<head>
<meta charset="utf-8">
<title>Bovrin-u Letterhead</title>
<link rel="stylesheet" href="https://fonts.googleapis.com/css2?family=Questrial&display=swap">
<style>
  :root {
    --brand-blue: #1d5a9e;
    --ink: #3a3a3a;
    --paper: #ffffff;
    --backdrop: #e8e8e9;
    --wash: rgba(29, 90, 158, 0.05);
  }
  * { box-sizing: border-box; margin: 0; padding: 0; }
  html, body {
    width: 1200px; height: 900px; overflow: hidden;
    background: var(--backdrop);
    font-family: "Questrial", sans-serif;
  }
  .letterhead {
    position: absolute; left: 303px; top: 30px;
    width: 594px; height: 840px;
    background: var(--paper);
    box-shadow: 0 6px 20px rgba(0,0,0,0.12);
    color: var(--ink);
    overflow: hidden;
  }
  .background-wash {
    position: absolute; left: -60px; top: 250px;
    width: 420px; height: 420px; border-radius: 50%;
    background: radial-gradient(circle, var(--wash) 0%, rgba(29,90,158,0.025) 55%, rgba(29,90,158,0) 72%);
  }
  .brand {
    position: absolute; left: 40px; top: 196px;
    color: var(--brand-blue);
    font-size: 22px; line-height: 1;
  }
  .address {
    position: absolute; right: 40px; top: 44px;
    text-align: right; font-size: 8px; line-height: 1.45;
    color: var(--brand-blue);
  }
  .letter-body {
    position: absolute; left: 205px; top: 300px; width: 340px;
    font-size: 9.2px; line-height: 1.5; text-align: justify;
  }
  .letter-body p + p { margin-top: 13px; }
  .sign-off { position: absolute; left: 240px; top: 610px; }
  .signature { display: block; width: 120px; height: 34px; }
  .sign-role { font-size: 10px; margin-top: 2px; }
  .contact-bar {
    position: absolute; left: 205px; bottom: 44px;
    display: flex; gap: 12px; align-items: stretch;
    font-size: 8.5px; line-height: 1.55; color: var(--brand-blue);
  }
  .contact-phones { display: flex; flex-direction: column; justify-content: flex-end; }
  .contact-divider { width: 1px; background: var(--brand-blue); }
  .contact-online { display: flex; flex-direction: column; }
  .contact-online span { display: flex; align-items: center; gap: 4px; }
  .icon { width: 8px; height: 8px; flex: none; }
  .footer-band {
    position: absolute; left: 0; right: 0; bottom: 0; height: 14px;
    background: var(--brand-blue);
  }
</style>
</head>
<body>
  <main class="letterhead">
    <div class="background-wash" role="img" aria-label="Faint brand watermark decoration"></div>

    <div class="address">
      Level 10, 27 Harlow Lane<br>
      Melbourne, Australia, 3000
    </div>

    <div class="brand">Bovrin-u</div>

    <section class="letter-body">
      <p>Letterhead samples are a great way of deciding what kind of letterhead you want to design for you and your company. The internet has a ton of great letterhead samples to browse through. Whether you want something simple, with just a couple lines of text of your business information, or something decorative and stunning, with photos and logos on the top and bottom of the page, it will be easy to find what you want, because there are samples online for basically any type of letterhead you could want.</p>
      <p>Any business could easily benefit from browsing through some letterhead samples, if only to get an idea for what kind of letterhead their company might want. Letterheads are just one of the tools that a business professional could use to help increase their customer base and to really be memorable to everyone they write a letter to. Letterhead is quite an effective tool for marketing and advertising, but because it's such a simple and well known idea, it is often unfairly overlooked. Make sure you don't make that mistake, and make some letterhead samples of your own today.</p>
      <p>Whether you want to get new customers to remember you and become part of your clientele, or you just want to send out friendly reminders to your existing clients, customizing your own letterhead samples can really help you out. Try out some letterhead samples and you will not regret it, and I'm sure you will add a new tool to your business' arsenal of networking, marketing, and advertising tools.</p>
    </section>

    <div class="sign-off">
      <svg class="signature" role="img" aria-label="Handwritten signature of Martin Halloway" viewBox="0 0 120 34">
        <rect x="0" y="4" width="120" height="26" rx="4" fill="var(--brand-blue)" opacity="0.18"/>
      </svg>
      <div class="sign-role">company director</div>
    </div>

    <div class="contact-bar">
      <div class="contact-phones">
        <span>P: +61 3 527 948 183</span>
        <span>F: +61 3 9042 5317</span>
      </div>
      <div class="contact-divider"></div>
      <div class="contact-online">
        <span>
          <svg class="icon" viewBox="0 0 8 8"><circle cx="4" cy="4" r="3.4" fill="none" stroke="var(--brand-blue)" stroke-width="1"/><path d="M0.6 4h6.8M4 0.6v6.8" stroke="var(--brand-blue)" stroke-width="0.7"/></svg>
          www.bovrin-u.com.au
        </span>
        <span>
          <svg class="icon" viewBox="0 0 8 8"><rect width="8" height="8" rx="1" fill="var(--brand-blue)"/></svg>
          @bovrin_u
        </span>
        <span>
          <svg class="icon" viewBox="0 0 8 8"><rect width="8" height="8" rx="1" fill="var(--brand-blue)"/></svg>
          /company/bovrin-u
        </span>
      </div>
    </div>

    <div class="footer-band"></div>
  </main>
</body>
</html>
```